Freelance business trainer needs a new business card

My business is called Brightpath. I provide training in the workplace on management, coaching and mentoring, and customer service topics for a variety of businesses, colleges and private training providers, and teach on management programs. I need a professional but eye catching business card. Business colours grey and orange. My name Linda Marrowby; Tel 07862 413057; email lmarrowby@brightpath.co.uk; website www.brightpath.co.uk.
Happy to have some sort of logo on front and details on back or all on one side
Target Market(s)
SME businesses and colleges - workshops i run are for adults in the workplace
Industry/Entity Type
Training
Look and feel
Each slider illustrates characteristics of the customer's brand and the style your logo design should communicate.

```html
<!DOCTYPE html>
<html lang="en">
<head>
<meta charset="utf-8">
<title>Brightpath – Linda Marrowby</title>
<link href="https://fonts.googleapis.com/css2?family=Playfair+Display+SC:wght@700&family=Tinos&display=swap" rel="stylesheet">
<style>
  :root {
    --card-grey: #4b5a5a;
    --ink: #111111;
    --orange-light: #f9a012;
    --orange-mid: #fb6a06;
    --orange-deep: #ff2200;
    --brand-orange: #f25c12;
    --icon-yellow: #ffe800;
    --detail-text: #d9e2e2;
  }
  html, body {
    margin: 0;
    padding: 0;
    width: 1200px;
    height: 720px;
    overflow: hidden;
    background: var(--card-grey);
  }
  .business-card {
    position: relative;
    width: 1200px;
    height: 720px;
    background: var(--card-grey);
  }
  .name-banner {
    position: absolute;
    left: 19px;
    top: 73px;
    width: 1156px;
    height: 209px;
    border: 3px solid var(--ink);
    background: linear-gradient(100deg, var(--orange-light) 0%, var(--orange-mid) 45%, var(--orange-deep) 100%);
  }
  .trainer-name {
    position: absolute;
    right: 28px;
    top: 58px;
    margin: 0;
    font-family: "Playfair Display SC", Georgia, serif;
    font-weight: 700;
    font-size: 78px;
    line-height: 1;
    letter-spacing: -1px;
    color: var(--ink);
  }
  .brand-name {
    position: absolute;
    left: 170px;
    top: 570px;
    margin: 0;
    font-family: "Playfair Display SC", Georgia, serif;
    font-weight: 700;
    font-size: 76px;
    line-height: 1;
    color: var(--brand-orange);
  }
  .contact-list {
    position: absolute;
    left: 650px;
    top: 350px;
    margin: 0;
    padding: 0;
    list-style: none;
  }
  .contact-item {
    display: flex;
    align-items: center;
    height: 56px;
    margin-bottom: 10px;
  }
  .contact-icon {
    width: 78px;
    height: 56px;
    flex: none;
  }
  .contact-text {
    margin-left: 12px;
    font-family: "Tinos", "Times New Roman", serif;
    font-size: 36px;
    letter-spacing: 0.5px;
    color: var(--detail-text);
  }
  .contact-text.phone {
    margin-left: 20px;
    letter-spacing: 2px;
  }
  .footer-band {
    position: absolute;
    left: 19px;
    top: 677px;
    width: 1156px;
    height: 18px;
    border: 3px solid var(--ink);
    background: linear-gradient(90deg, var(--orange-light) 0%, var(--orange-mid) 45%, var(--orange-deep) 100%);
  }
</style>
</head>
<body>
<main class="business-card">
  <header class="name-banner">
    <h1 class="trainer-name">Linda Marrowby</h1>
  </header>

  <p class="brand-name">Brightpath</p>

  <ul class="contact-list">
    <li class="contact-item">
      <svg class="contact-icon" viewBox="0 0 78 56" aria-hidden="true">
        <ellipse cx="39" cy="28" rx="36" ry="25" fill="var(--orange-mid)" stroke="var(--ink)" stroke-width="3"/>
        <path d="M30 12 l8 -2 l4 10 l-5 4 q3 8 10 12 l5 -4 l9 6 l-3 8 q-14 2 -24 -12 q-8 -12 -4 -22 z"
              fill="var(--icon-yellow)" stroke="var(--ink)" stroke-width="2.5" stroke-linejoin="round"/>
      </svg>
      <span class="contact-text phone">07862 413057</span>
    </li>
    <li class="contact-item">
      <svg class="contact-icon" viewBox="0 0 78 56" aria-hidden="true">
        <ellipse cx="39" cy="28" rx="36" ry="25" fill="var(--orange-mid)" stroke="var(--ink)" stroke-width="3"/>
        <rect x="20" y="16" width="38" height="25" fill="var(--icon-yellow)" stroke="var(--ink)" stroke-width="2.5"/>
        <path d="M20 16 L39 31 L58 16 M20 41 L33 27 M58 41 L45 27" fill="none" stroke="var(--ink)" stroke-width="2.5"/>
      </svg>
      <span class="contact-text">lmarrowby@brightpath.co.uk</span>
    </li>
    <li class="contact-item">
      <svg class="contact-icon" viewBox="0 0 78 56" aria-hidden="true">
        <ellipse cx="39" cy="28" rx="36" ry="25" fill="var(--orange-mid)" stroke="var(--ink)" stroke-width="3"/>
        <g fill="none" stroke="var(--ink)" stroke-width="2.5">
          <circle cx="39" cy="28" r="17"/>
          <ellipse cx="39" cy="28" rx="7" ry="17"/>
          <line x1="39" y1="11" x2="39" y2="45"/>
          <line x1="22" y1="28" x2="56" y2="28"/>
          <path d="M25 19 H53 M25 37 H53"/>
        </g>
      </svg>
      <span class="contact-text">www.brightpath.co.uk</span>
    </li>
  </ul>

  <div class="footer-band"></div>
</main>
</body>
</html>
```